Marlowvane Services Website Design

We have most content but require a professional design. We have a logo already and will need it utilized along with several of the photos from the attached documentation.
First page should have our mission and Vision and the synapsis provided in the word document. Visitors will be prompted to select from one of our 3 divisions from this page.
Each division will have the same list of tabs : About, Services, Safety, Careers and Contact.
Photos on each divisions page should be representative of the divisions offerings. The word doc attached contains the requested content and we are open to edits that would complement and fill the website.
I like the Tornwick site www.tornwick-example.com - they are our competition so cant be modeled directly after this.
Please include prompts to request quote at each service page. align the format of the geotechnical page to the other 2 divisions.
I used chat gpt for some of the content so will need it optimized for SCO.

```html
<!DOCTYPE html>
<html lang="en">
<head>
<meta charset="utf-8">
<title>Marlowvane Services</title>
<link href="https://fonts.googleapis.com/css2?family=Manrope:wght@400;500;600;700&display=swap" rel="stylesheet">
<style>
:root{
  --red:#e8202a;
  --ink:#1e1e1f;
  --black:#000;
  --card:#0d0d0d;
  --white:#fff;
  --muted:#8a8a8a;
  --soft:#cfcfcf;
}
*{box-sizing:border-box;margin:0;padding:0}
html,body{width:1200px;height:3599px;overflow:hidden;background:var(--ink)}
body{font-family:'Manrope',sans-serif;color:var(--white)}
.page{position:relative;width:1200px;height:3599px}
section,footer{position:relative;width:1200px;overflow:hidden}
.abs{position:absolute}
.red{color:var(--red)}
.section-title{position:absolute;left:0;width:100%;text-align:center;font-size:29px;font-weight:500}
.btn-outline{position:absolute;left:538px;width:124px;height:34px;border:1.5px solid var(--red);border-radius:17px;color:var(--red);font-size:10px;display:flex;align-items:center;justify-content:center}
.btn-red{position:absolute;height:34px;border-radius:17px;background:var(--red);color:var(--white);font-size:10px;font-weight:600;display:flex;align-items:center;justify-content:center}

/* hero */
.hero{height:519px}
.hero-photo{position:absolute;inset:0;background:linear-gradient(180deg,#4b5560 0%,#3a4038 30%,#5a4e42 62%,#3b332c 100%)}
.hero-shade{position:absolute;inset:0;background:linear-gradient(90deg,rgba(0,0,0,.45),rgba(0,0,0,.1))}
.brand{position:absolute;left:75px;top:20px;font-size:30px;font-weight:700;letter-spacing:3px;color:var(--red)}
.nav{position:absolute;top:26px;left:480px;right:75px;display:flex;align-items:center;gap:36px;font-size:11px;font-weight:500}
.nav .active{color:var(--red)}
.nav .quote{margin-left:auto;border:1.5px solid var(--white);border-radius:18px;padding:10px 22px}
.hero h1{position:absolute;left:138px;top:208px;font-size:38px;font-weight:700}
.hero .lead{position:absolute;left:138px;top:254px;width:420px;font-size:28px;line-height:38px;font-weight:400}
.slide-btn{position:absolute;top:484px;width:36px;height:35px;background:var(--white);color:#222;font-size:16px;display:flex;align-items:center;justify-content:center}

/* services */
.services{height:478px;background:var(--ink)}
.service-row{position:absolute;top:142px;left:76px;display:flex;gap:27px}
.service-card{width:189px;height:164px;background:var(--card);display:flex;flex-direction:column;align-items:center;justify-content:center;gap:16px;font-size:13px;font-weight:600}
.service-card.on{background:var(--red)}
.service-card svg{width:64px;height:64px}

/* vision & mission */
.vision{height:721px;background:var(--black)}
.vision-text{position:absolute;left:250px;width:700px;top:124px;text-align:center;font-size:13px;line-height:22px;color:var(--muted)}
.mission-title{position:absolute;left:138px;top:282px;font-size:29px;font-weight:500}
.mission-text{position:absolute;left:138px;top:340px;width:460px;font-size:13px;line-height:25px;color:var(--muted)}
.mission-photo{position:absolute;left:661px;top:214px;width:412px;height:434px;background:linear-gradient(180deg,#c9ced3 0%,#b8bdc2 48%,#8c8a85 72%,#7a7770 100%);border:1px solid #444}

/* divisions */
.divisions{height:595px;background:var(--ink)}
.division{position:absolute;top:148px;width:250px;height:307px;display:flex;align-items:flex-end;justify-content:center;padding-bottom:24px;font-size:13px;font-weight:600}

/* careers */
.careers{height:287px;background:var(--red)}
.careers h2{position:absolute;left:138px;top:55px;font-size:29px;font-weight:500}
.careers p{position:absolute;left:138px;top:113px;width:450px;font-size:17px;line-height:22px}
.careers .apply{position:absolute;left:138px;top:200px;width:124px;height:34px;border-radius:17px;background:var(--white);color:var(--red);font-size:10px;font-weight:600;display:flex;align-items:center;justify-content:center}
.careers .mark{position:absolute;left:676px;top:106px;font-size:58px;font-weight:700;letter-spacing:4px;color:var(--white)}

/* articles */
.articles{height:628px;background:var(--ink)}
.article{position:absolute}
.article .img{width:100%}
.article h3{font-size:14px;font-weight:500;line-height:19px;margin-top:18px}
.article p{font-size:10px;line-height:16px;color:var(--muted);margin-top:10px}

/* footer */
.footer{height:371px;background:linear-gradient(180deg,#1a1a1a,#242424 60%,#1a1a1a)}
.footer .logo{position:absolute;left:138px;top:124px;font-size:26px;font-weight:700;letter-spacing:3px}
.fcol{position:absolute;top:120px;font-size:10px;line-height:22px}
.fcol h4{font-size:12px;font-weight:600;margin-bottom:12px}
.fcol .row{display:flex;align-items:flex-start;gap:12px}
.fcol svg{width:12px;height:12px;margin-top:5px;flex:none}
.links{display:grid;grid-template-columns:72px 90px}
.social{display:flex;gap:6px}
.social span{width:22px;height:22px;border-radius:50%;background:#6d6d6d}
.social span.on{background:var(--red)}
.footer .rule{position:absolute;left:75px;right:75px;top:310px;border-top:1px solid #3a3a3a}
.footer .copy{position:absolute;left:0;width:100%;top:333px;text-align:center;font-size:10px}
</style>
</head>
<body>
<div class="page">

<section class="hero">
  <div class="hero-photo" role="img" aria-label="Photo of a white aerial boom truck parked on a dirt lot with a building and trees behind"></div>
  <div class="hero-shade"></div>
  <div class="brand">MARLOWVANE</div>
  <nav class="nav">
    <span class="active">Home</span><span>About Us</span><span>Services</span><span>Divisions</span><span>Contact Us</span>
    <span>&#9742; (555) 014-2280</span>
    <span class="quote">Request a Quote</span>
  </nav>
  <h1>Marlowvane</h1>
  <p class="lead">Your Partner in Wind Turbine Performance!</p>
  <div class="btn-red" style="left:138px;top:352px;width:123px">Our Services</div>
  <svg class="abs" style="left:794px;top:448px" width="12" height="40" viewBox="0 0 12 40"><path d="M6 0v36M1 31l5 6 5-6" stroke="#fff" stroke-width="1.5" fill="none"/></svg>
  <div class="slide-btn" style="left:985px">&#8249;</div>
  <div class="slide-btn" style="left:1026px">&#8250;</div>
</section>

<section class="services">
  <h2 class="section-title" style="top:74px">Marlowvane <span class="red">Services</span></h2>
  <div class="service-row">
    <div class="service-card">
      <svg viewBox="0 0 64 64" fill="none" stroke="#fff" stroke-width="2"><path d="M32 6l18 7v14c0 12-8 20-18 24-10-4-18-12-18-24V13z"/><circle cx="32" cy="28" r="8" fill="#e8202a" stroke="none"/><path d="M8 50h48l-4 8H12z"/></svg>
      Delivering safe</div>
    <div class="service-card on">
      <svg viewBox="0 0 64 64" fill="none" stroke="#fff" stroke-width="2"><path d="M10 50V14M22 50V14M10 14h12M10 26h12M10 38h12M22 20l24 16M46 36v8"/><path d="M6 56h52v4H6z" fill="#000" stroke="none"/></svg>
      Oil&amp;Gas</div>
    <div class="service-card">
      <svg viewBox="0 0 64 64" fill="none" stroke="#fff" stroke-width="2"><path d="M16 58V8h28M16 14h30M38 14v14"/><rect x="28" y="30" width="20" height="28" fill="#e8202a" stroke="#fff"/><path d="M28 44h20M38 30v28"/></svg>
      Construction</div>
    <div class="service-card">
      <svg viewBox="0 0 64 64" fill="none" stroke="#fff" stroke-width="2"><path d="M32 4l-12 54M32 4l12 54M18 18h28M16 30h32M22 44h20"/><circle cx="32" cy="24" r="4" fill="#e8202a" stroke="none"/></svg>
      Utility</div>
    <div class="service-card">
      <svg viewBox="0 0 64 64" fill="none" stroke="#fff" stroke-width="2"><path d="M32 28L14 8M32 28l22-10M32 28L30 54M32 28v30M24 58h16"/><circle cx="32" cy="28" r="4" fill="#e8202a" stroke="none"/></svg>
      Renewable energy</div>
  </div>
  <div class="btn-outline" style="top:339px">Explore More</div>
</section>

<section class="vision">
  <h2 class="section-title" style="top:68px">Our <span class="red">Vision</span></h2>
  <p class="vision-text">To be the leading provider of aerial access, geotechnical drilling, and service solutions, setting the standard for excellence in safety, efficiency, and environmental stewardship.</p>
  <h2 class="mission-title">Our <span class="red">Mission</span></h2>
  <p class="mission-text">At Marlowvane, our mission is to deliver unparalleled aerial access, geotechnical drilling, and service and maintenance solutions, consistently exceeding our clients' expectations. We strive to achieve this by investing in cutting-edge technology, fostering a culture of safety and continuous improvement, and prioritizing environmental sustainability. Through collaboration, integrity, and dedication, we aim to contribute to the success of our clients while maintaining the highest standards of quality and professionalism.</p>
  <div class="mission-photo" role="img" aria-label="Photo of two white boom trucks parked on gravel under an overcast sky"></div>
</section>

<section class="divisions">
  <h2 class="section-title" style="top:74px">Select <span class="red">Division</span></h2>
  <div class="division" style="left:201px;background:linear-gradient(180deg,#2e5fae 0%,#8fb2dc 50%,#3c6db4 100%)" role="img" aria-label="Photo of an aerial work basket against a blue cloudy sky">Aerial Access</div>
  <div class="division" style="left:475px;background:linear-gradient(180deg,#7d9cc4 0%,#b7cbe0 55%,#8e6f6a 100%)" role="img" aria-label="Photo of a tall drilling mast against a pale sky">Geotechnical Drilling</div>
  <div class="division" style="left:751px;background:linear-gradient(180deg,#3e7bc8 0%,#79a9d8 45%,#c99a2e 65%,#1f5c9a 100%)" role="img" aria-label="Photo of an offshore energy platform on blue water">Renewable Energy Services</div>
  <div class="btn-red" style="left:538px;top:488px;width:124px">Request a Quote</div>
</section>

<section class="careers">
  <h2>Careers</h2>
  <p>We are always looking for skilled blade technicians, wind turbine maintenance technicians to join our team.</p>
  <div class="apply">Apply Now</div>
  <div class="mark">MARLOWVANE</div>
</section>

<section class="articles">
  <h2 class="section-title" style="top:74px">Recent <span class="red">Articles</span></h2>
  <div class="article" style="left:138px;top:168px;width:244px">
    <div class="img" style="height:215px;background:linear-gradient(180deg,#9bbbe0,#5d7da3 60%,#334a66)" role="img" aria-label="Photo looking up at glass skyscrapers"></div>
    <h3>There are many variations of passages of lorem Ipsum available</h3>
  </div>
  <div class="article" style="left:408px;top:137px;width:386px">
    <div class="img" style="height:277px;background:linear-gradient(180deg,#e8e6e2,#cfc9c0 55%,#8f6a45)" role="img" aria-label="Photo of a small house model on blueprints with a hard hat"></div>
    <h3>Contrary to popular belief</h3>
    <p>There are many variations of passages of lorem ipsum available,<br>but the majority.</p>
  </div>
  <div class="article" style="left:820px;top:168px;width:244px">
    <div class="img" style="height:215px;background:linear-gradient(180deg,#3a3a3d,#a9bdd6 35%,#7f8794 70%,#4a4e55)" role="img" aria-label="Photo of a highway overpass seen from under a bridge"></div>
    <h3>There are many variations of passages of lorem Ipsum available</h3>
  </div>
  <div class="btn-outline" style="top:520px">View All</div>
</section>

<footer class="footer" role="img" aria-label="Dark aerial photo of a work site behind the footer">
  <div class="logo">MARLOWVANE</div>
  <div class="fcol" style="left:408px">
    <h4>Contact Us</h4>
    <div class="row" style="font-size:14px"><svg viewBox="0 0 12 12"><path d="M2 1l3 1 1 3-2 1c1 2 2 3 4 4l1-2 3 1 0 3c-6 0-10-4-10-10z" fill="#e8202a"/></svg>(555) 014-2280</div>
    <div class="row"><svg viewBox="0 0 12 12"><rect x="1" y="2" width="10" height="8" fill="#e8202a"/></svg>info@marlowvane-example.com</div>
    <div class="row" style="line-height:14px;margin-top:6px"><svg viewBox="0 0 12 12"><path d="M6 0a4 4 0 0 1 4 4c0 3-4 8-4 8S2 7 2 4a4 4 0 0 1 4-4z" fill="#e8202a"/></svg>118 Ridgeline Road Alder Falls<br>AB X0X-0X0</div>
  </div>
  <div class="fcol" style="left:665px">
    <h4>Quick Links</h4>
    <div class="links"><span>Home</span><span>Careers</span><span>About Us</span><span>News</span><span>Services</span><span>Term &amp; Conditions</span><span>Divisions</span><span>Privacy Policy</span><span>Contact Us</span></div>
  </div>
  <div class="fcol" style="left:885px">
    <h4>Follow Us</h4>
    <div class="social"><span></span><span class="on"></span><span></span><span></span></div>
  </div>
  <svg class="abs" style="left:1124px;top:146px" width="14" height="12" viewBox="0 0 14 12"><path d="M7 0l7 12H0z" fill="#e8202a"/></svg>
  <div class="rule"></div>
  <div class="copy">© 2024 <span class="red">Marlowvane</span>. All Rights Reserved</div>
</footer>

</div>
</body>
</html>
```